Morrow Engineering Core Values Branding Package

Morrow Engineering has recently refined its company Core Values and is seeking a strong, cohesive branding package to visually bring these values to life. The new graphic assets will communicate our commitment to excellence in a way that resonates with our team, clients, and partners in a blue-collar, industrial environment.

We are looking for multiple visual assets with consistent design elements that can be applied across platforms. The tone should reflect strength, reliability, and professionalism while remaining approachable and aligned with our industry.

Core Values & Descriptions
Accountability
“We take ownership of our work and actions, ensuring reliability and trust in every solution we deliver.”

Teamwork
“We collaborate across departments and disciplines to provide the highest level of service and innovation for our clients.”

Integrity
“We operate with honesty, transparency, and ethical standards in all aspects of our business.”

Growth
“We are committed to continuous improvement—of our people, our processes, and our impact in the industry.”

Deliverables

1. Primary Core Values Graphic
A master visual representing all four values together.
Designed for use on posters, office signage, internal presentations.

2. Individual Value Graphics (x4)
One graphic per core value: Accountability, Teamwork, Integrity, Growth.
Cohesive style with slight visual variation to reflect each value’s unique meaning.

Target Market(s)

Employees of Morrow Engineering

Industry/Entity Type

Blue Collar

Font styles to use
Sans Serif

Colors
0054AA
0677BA
7BADD7
CADEEF
E8F1F8
00AB8E
00BBA5
67D7C9
C6EFE9
E9F9F6
EB3D1F
EC4F4E
F09395
F8D3D4
FCEDEE

Requirements
Must have
• Accountability, Teamwork, Integrity, Growth

```html
<!DOCTYPE html>
<html lang="en">
<head>
<meta charset="utf-8">
<title>Morrow Engineering – Core Value</title>
<link href="https://fonts.googleapis.com/css2?family=Roboto+Condensed:wght@400;700&display=swap" rel="stylesheet">
<style>
  :root {
    --navy: #0b2f67;
    --navy-deep: #082757;
    --green: #3bae49;
    --green-soft: #9fd6a3;
    --sky: #bcd7ef;
    --ink: #0b2f67;
    --stage: #b3b3b3;
    --paper: #ffffff;
    --orange: #f29a2e;
  }
  * { margin: 0; padding: 0; box-sizing: border-box; }
  html, body { width: 1200px; height: 2434px; overflow: hidden; }
  body {
    background: var(--stage);
    font-family: "Roboto Condensed", "Arial Narrow", sans-serif;
    position: relative;
  }
  .poster {
    position: absolute;
    left: 0; top: 375px;
    width: 1200px; height: 1684px;
    background: var(--paper);
    overflow: hidden;
  }
  .poster-shapes, .hero-photo { position: absolute; left: 0; top: 0; }
  .brand-name {
    position: absolute; left: 0; right: 0; top: 100px;
    text-align: center;
    font-size: 118px; font-weight: 700; letter-spacing: 2px;
    color: var(--navy); line-height: 1;
  }
  .headline {
    position: absolute; left: 0; right: 0; top: 826px;
    text-align: center;
    font-size: 200px; font-weight: 700; line-height: 1;
    color: var(--green); letter-spacing: 2px;
  }
  .values {
    position: absolute; left: 0; top: 1190px; width: 1200px;
  }
  .value {
    position: absolute; width: 240px; margin-left: -120px;
    text-align: center; color: var(--ink);
  }
  .value-title { font-size: 33px; font-weight: 700; line-height: 1.1; }
  .value-text { font-size: 26px; font-weight: 400; line-height: 30.5px; }
  .value.accountability { left: 224px; }
  .value.teamwork { left: 466px; width: 230px; margin-left: -115px; }
  .value.integrity { left: 724px; width: 260px; margin-left: -130px; }
  .value.growth { left: 989px; width: 240px; }
  .site {
    position: absolute; left: 0; right: 0; top: 1592px;
    text-align: center; color: #fff;
    font-size: 52px; font-weight: 700; letter-spacing: 1px;
  }
</style>
</head>
<body>
<main class="poster">
  <svg class="poster-shapes" width="1200" height="1684" viewBox="0 0 1200 1684" aria-hidden="true">
    <defs>
      <linearGradient id="topWash" x1="0" y1="0" x2="1" y2="1">
        <stop offset="0" stop-color="#eef6ee"/>
        <stop offset="1" stop-color="#ffffff"/>
      </linearGradient>
      <linearGradient id="greenBand" x1="0" x2="1">
        <stop offset="0" stop-color="#3bae49"/>
        <stop offset="0.6" stop-color="#55b960"/>
        <stop offset="1" stop-color="#a6d9aa"/>
      </linearGradient>
    </defs>
    <rect width="1200" height="360" fill="url(#topWash)"/>
    <path d="M0 352 Q600 300 1200 352 L1200 382 Q600 332 0 380 Z" fill="url(#greenBand)"/>
    <!-- bottom sweep -->
    <path d="M0 1010 C20 1300 160 1530 480 1560 C780 1585 1000 1460 1200 1360 L1200 1684 L0 1684 Z" fill="var(--navy)"/>
    <path d="M0 1010 C20 1300 160 1530 480 1560 C780 1585 1000 1460 1200 1360" fill="none" stroke="var(--sky)" stroke-width="12"/>
    <path d="M180 1468 Q380 1560 580 1502" fill="none" stroke="var(--green)" stroke-width="6" stroke-linecap="round"/>
    <!-- value connector line -->
    <line x1="109" y1="1098" x2="1107" y2="1098" stroke="#555" stroke-width="1.5"/>
    <!-- icon discs -->
    <g fill="var(--navy)" stroke="#e7eef7" stroke-width="3">
      <circle cx="224" cy="1098" r="75"/>
      <circle cx="466" cy="1098" r="75"/>
      <circle cx="724" cy="1098" r="75"/>
      <circle cx="989" cy="1098" r="75"/>
    </g>
    <!-- accountability: hand holding chart with tick -->
    <g fill="none" stroke="var(--green)" stroke-width="3" stroke-linecap="round" stroke-linejoin="round">
      <rect x="204" y="1058" width="36" height="46"/>
      <path d="M212 1096 v-10 M222 1096 v-18 M232 1096 v-24"/>
      <path d="M190 1110 q20 16 44 8 l30 -20"/>
      <circle cx="216" cy="1058" r="8" stroke="var(--orange)"/>
      <path d="M212 1058 l3 3 6 -6" stroke="var(--orange)"/>
    </g>
    <!-- teamwork: people around cycle -->
    <g fill="none" stroke="var(--green)" stroke-width="3" stroke-linecap="round">
      <circle cx="466" cy="1068" r="8"/>
      <circle cx="440" cy="1074" r="7"/>
      <circle cx="492" cy="1074" r="7"/>
      <path d="M452 1090 q14 -14 28 0 M428 1094 q12 -12 24 0 M480 1094 q12 -12 24 0"/>
      <path d="M452 1118 a16 16 0 0 1 26 -14 M482 1120 a16 16 0 0 1 -26 12" stroke="var(--orange)"/>
    </g>
    <!-- integrity: arrow into gear -->
    <g fill="none" stroke="var(--green)" stroke-width="3" stroke-linecap="round" stroke-linejoin="round">
      <circle cx="744" cy="1098" r="26"/>
      <path d="M690 1084 h30 M686 1098 h44 M690 1112 h30"/>
      <path d="M728 1086 l16 12 -16 12" stroke="var(--orange)"/>
    </g>
    <!-- growth: bar chart with rising arrow -->
    <g fill="none" stroke="var(--green)" stroke-width="3" stroke-linecap="round" stroke-linejoin="round">
      <path d="M952 1128 v-10 h10 v10 M968 1128 v-18 h10 v18 M984 1128 v-26 h10 v26 M1000 1128 v-36 h10 v36 M1016 1128 v-46 h10 v46"/>
      <path d="M950 1106 l30 -22 14 8 28 -26"/>
      <path d="M1012 1066 h10 v10"/>
      <circle cx="968" cy="1072" r="11" stroke="var(--orange)"/>
    </g>
  </svg>

  <svg class="hero-photo" width="1200" height="800" viewBox="0 0 1200 800" role="img" aria-label="Photograph of a data centre corridor lined with rows of server racks">
    <defs>
      <linearGradient id="photoTone" x1="0" x2="1">
        <stop offset="0" stop-color="#1f3135"/>
        <stop offset="0.35" stop-color="#5f6d70"/>
        <stop offset="0.7" stop-color="#c9d3d6"/>
        <stop offset="1" stop-color="#6f7b7e"/>
      </linearGradient>
    </defs>
    <path d="M0 378 Q600 330 1200 380 L1200 797 L0 797 Z" fill="url(#photoTone)"/>
  </svg>

  <div class="brand-name">MORROW</div>
  <h1 class="headline">CORE VALUE</h1>

  <section class="values">
    <div class="value accountability">
      <h2 class="value-title">Accountability</h2>
      <p class="value-text">We take ownership<br>of our work and<br>actions, ensuring<br>reliability and trust<br>in every solution<br>we deliver.</p>
    </div>
    <div class="value teamwork">
      <h2 class="value-title">Teamwork</h2>
      <p class="value-text">We collaborate across<br>departments and<br>disciplines to provide<br>the highest level<br>of service and<br>innovation for our<br>clients.</p>
    </div>
    <div class="value integrity">
      <h2 class="value-title">Integrity</h2>
      <p class="value-text">We operate with honesty,<br>transparency, and<br>ethical standards<br>in all aspects<br>of our business.</p>
    </div>
    <div class="value growth">
      <h2 class="value-title">Growth</h2>
      <p class="value-text">We are committed<br>to continuous<br>improvement-of our<br>people, our processes,<br>and our impact in the<br>industry.</p>
    </div>
  </section>

  <p class="site">www.morrow-eng.com</p>
</main>
</body>
</html>
```